Hello,
Marisol Trent Equestrian needs a business card. We are a high performance show jumping stables based at Oakhollow Paddocks in morningotn. We pride ourselves on producing high quality show jumping horses and competing our stock at a high level. My business card need to have my logo on it, and i would like it to have a classic design with a modern touch. I would like it to have quite a natural feel about it. It needs to be in a font which is easy to read as I spend a lot of time competing internationally and overseas, and i need to be able to give it out to breeders and contacts where English isnt their first language. I will need it to include the following details:
-Marisol Trent Equestrian
-Based at Oakhollow Paddocks Mornington
-Address: 17 Pemberly Lane Mornington Victoria 3931
-Mobile number: 0412659048
- website: www.marisoltrentequestrian-example.com
Target Market(s)
For business adults who english may not be their first language
Industry/Entity Type
Business

```html
<!DOCTYPE html>
<html lang="en">
<head>
<meta charset="utf-8">
<title>Marisol Trent Equestrian – Business Card</title>
<link rel="stylesheet" href="https://fonts.googleapis.com/css2?family=Cinzel:wght@400;700&display=swap">
<style>
  :root {
    --stage: #e9e6e1;
    --card-black: #0b0b0b;
    --gold: #f2d21c;
    --ink: #111111;
    --sky: #e6ecf5;
    --haze: #d4dde0;
    --field: #b9c7a6;
    --field-deep: #9fb18a;
  }
  * { box-sizing: border-box; margin: 0; padding: 0; }
  html, body { width: 1200px; height: 900px; overflow: hidden; }
  body {
    background: var(--stage);
    font-family: "Cinzel", Georgia, serif;
    display: flex;
    flex-direction: column;
    align-items: center;
    justify-content: center;
    gap: 48px;
  }
  .card {
    position: relative;
    width: 630px;
    height: 360px;
    border-radius: 6px;
    overflow: hidden;
    box-shadow: 0 10px 30px rgba(0,0,0,0.18);
  }

  /* Front */
  .card-front { background: var(--card-black); }
  .card-front .frame {
    position: absolute;
    inset: 18px;
    border: 2px solid var(--gold);
  }
  .card-front .brand {
    position: absolute;
    inset: 0;
    display: flex;
    flex-direction: column;
    align-items: center;
    justify-content: center;
    gap: 26px;
    color: var(--gold);
  }
  .brand-mark {
    display: flex;
    align-items: center;
    gap: 12px;
    font-size: 22px;
    letter-spacing: 1px;
  }
  .brand-mark .dot {
    width: 16px; height: 16px; border-radius: 50%;
    background: var(--gold);
  }
  .card-front .brand-name {
    font-size: 34px;
    letter-spacing: 1px;
  }

  /* Back */
  .card-back { background: #f4f6f8; }
  .card-back .landscape {
    position: absolute;
    inset: 0;
    background: linear-gradient(180deg,
      var(--sky) 0%, var(--sky) 38%,
      var(--haze) 52%,
      var(--field) 66%, var(--field-deep) 100%);
  }
  .card-back .details {
    position: absolute;
    left: 36px;
    bottom: 34px;
    color: var(--ink);
  }
  .card-back .back-mark {
    display: flex;
    align-items: center;
    gap: 10px;
    font-size: 17px;
    margin-bottom: 10px;
  }
  .card-back .back-mark .dot {
    width: 12px; height: 12px; border-radius: 50%;
    background: var(--ink);
  }
  .card-back .based {
    font-weight: 700;
    font-size: 17px;
    margin-bottom: 26px;
  }
  .contact-list { list-style: none; }
  .contact-list li {
    display: flex;
    align-items: center;
    gap: 10px;
    font-size: 15px;
    font-weight: 700;
    line-height: 1.6;
  }
  .contact-list svg { width: 14px; height: 14px; flex: none; }
</style>
</head>
<body>

  <section class="card card-front" aria-label="Card front">
    <div class="frame"></div>
    <div class="brand">
      <div class="brand-mark"><span class="dot"></span>Marisol Trent Equestrian</div>
      <h1 class="brand-name">Marisol Trent Equestrian</h1>
    </div>
  </section>

  <section class="card card-back" aria-label="Card back">
    <div class="landscape" role="img" aria-label="Photograph of open green paddocks with a large gum tree under a pale sky"></div>
    <div class="details">
      <div class="back-mark"><span class="dot"></span>Marisol Trent Equestrian</div>
      <p class="based">Based at Oakhollow Paddocks Mornington</p>
      <ul class="contact-list">
        <li>
          <svg viewBox="0 0 14 14" aria-hidden="true"><rect x="3" y="0.5" width="8" height="13" rx="1.5" fill="var(--ink)"/><rect x="4.5" y="2" width="5" height="8" fill="#fff"/></svg>
          0412659048
        </li>
        <li>
          <svg viewBox="0 0 14 14" aria-hidden="true" fill="none" stroke="var(--ink)" stroke-width="1.3"><circle cx="7" cy="7" r="6"/><ellipse cx="7" cy="7" rx="2.6" ry="6"/><line x1="1" y1="7" x2="13" y2="7"/></svg>
          www.marisoltrentequestrian-example.com
        </li>
        <li>
          <svg viewBox="0 0 14 14" aria-hidden="true"><path d="M7 1 L13 7 H11 V13 H8.5 V9 H5.5 V13 H3 V7 H1 Z" fill="var(--ink)"/></svg>
          17 Pemberly Lane Mornington Victoria 3931
        </li>
      </ul>
    </div>
  </section>

</body>
</html>
```